Two Page, Multi Product Industrial Flyer

We are looking for a two page, 8.5" x 11" flyer for print and web.
300 DPI, PSD

For the following products (in the psd)
All the information required is in the psd, grouped and organized.
Also include our logo/header, the dustbox/corvel logos, qr code, and the following text;

Prices Valid until December 31st, 2015
Hours of Operation: Mon-Fri: 6:30am - 5:00pm | Saturday: 7:30am - 12:00pm
Save Time, Buy Online

NOTE: all sku's starting in "COR" are corvel brand, all sku's starting in "DBX" are dust box.

You can also combine a few skus, if need be
one picture, multiple skus/descriptions, price (folders labeled as "combine")

Target Market(s)

industrial contractors

Industry/Entity Type

Industrial

Font styles to use
Sans Serif

Requirements
Nice to have
• other flyers we currently have, for ideas;
• (this flyer does not have to conform to any of these flyers, just for ideas)
• http://qr-w.example/specials
• Here are some 'good examples'
• http://qr-w.example/wp-content/uploads/ML15-1615-FINAL-Building-Anchors-Swap-In-2.jpg
• http://qr-w.example/wp-content/uploads/2015-09-01-Brenton-Warm-Wear.jpg
Should not have
• These ones aren't so good;
• http://qr-w.example/wp-content/uploads/Lorv-Sanders.jpg
• http://qr-w.example/wp-content/uploads/2015-09-23-October.jpg

```html
<!DOCTYPE html>
<html lang="en">
<head>
<meta charset="utf-8">
<title>Northgate Bolts &amp; Tools – Save Time, Buy Online</title>
<link rel="stylesheet" href="https://fonts.googleapis.com/css2?family=Roboto+Condensed:wght@400;700&family=Roboto:wght@400;900&family=Lato:wght@400;700&display=swap">
<style>
  :root {
    --green: #1fa33a;
    --ink: #1b1b1b;
    --dark-top: #2e2e2e;
    --dark-bottom: #141414;
    --paper: #ffffff;
    --tab-grey: #d9d9d9;
    --rule: #e4e4e4;
    --accent-red: #d8242c;
  }
  * { box-sizing: border-box; margin: 0; padding: 0; }
  html, body { width: 963px; height: 1200px; overflow: hidden; background: var(--paper); }
  .flyer {
    position: relative;
    width: 963px; height: 1200px;
    overflow: hidden;
    font-family: "Roboto Condensed", "Arial Narrow", sans-serif;
  }
  .flyer__shapes { position: absolute; inset: 0; }

  .brand { position: absolute; left: 22px; top: 86px; display: flex; align-items: center; gap: 14px; }
  .brand__mark { width: 62px; height: 62px; background: var(--ink); }
  .brand__name {
    color: var(--green); font-weight: 700; font-size: 34px; line-height: 36px;
    text-transform: uppercase; letter-spacing: 0.5px;
  }

  .headline { position: absolute; left: 36px; top: 232px; }
  .headline__main {
    color: var(--green); font-weight: 700; font-size: 86px; line-height: 92px; text-transform: uppercase;
  }
  .headline__sub {
    font-family: "Roboto", Arial, sans-serif; color: var(--ink); font-weight: 400;
    font-size: 62px; line-height: 66px; text-transform: uppercase; letter-spacing: 1px;
  }

  .validity { position: absolute; left: 36px; top: 500px; text-transform: uppercase; }
  .validity__lead { color: var(--paper); font-weight: 700; font-size: 77px; line-height: 82px; }
  .validity__month { color: var(--green); font-weight: 700; font-size: 59px; line-height: 68px; letter-spacing: 0.5px; }
  .validity__date { font-family: "Roboto", Arial, sans-serif; color: var(--paper); font-size: 78px; line-height: 88px; letter-spacing: 3px; }
  .validity__day { font-weight: 900; }
  .validity__year { font-weight: 400; }

  .hours__title {
    position: absolute; right: 16px; top: 780px;
    color: var(--ink); font-weight: 700; font-size: 36px; line-height: 42px; text-transform: uppercase;
  }
  .hours__list { position: absolute; left: 673px; top: 856px; font-family: "Lato", Arial, sans-serif; }
  .hours__day { color: var(--paper); font-weight: 700; font-size: 54px; line-height: 58px; text-transform: uppercase; }
  .hours__time { color: var(--green); font-weight: 700; font-size: 30px; line-height: 36px; margin-bottom: 10px; }

  .partners { position: absolute; left: 37px; top: 1072px; display: flex; align-items: center; gap: 56px; }
  .partner { display: flex; align-items: center; gap: 10px; color: var(--paper); font-weight: 700; font-size: 38px; line-height: 44px; text-transform: uppercase; }
  .partner__square { width: 28px; height: 28px; background: var(--accent-red); }

  .contact {
    position: absolute; right: 16px; top: 1107px;
    font-family: "Lato", Arial, sans-serif; font-style: normal; color: var(--paper); font-size: 19px; line-height: 28px;
    text-align: right;
  }
  .contact__row { display: flex; justify-content: flex-end; align-items: center; gap: 8px; }
  .contact__icon { width: 16px; height: 16px; fill: none; stroke: var(--paper); stroke-width: 2; }
  .contact__row--last { padding-right: 24px; }
</style>
</head>
<body>
<main class="flyer">
  <svg class="flyer__shapes" width="963" height="1200" viewBox="0 0 963 1200">
    <defs>
      <linearGradient id="darkPanel" x1="0" y1="0" x2="0" y2="1">
        <stop offset="0" stop-color="#2e2e2e"/>
        <stop offset="1" stop-color="#141414"/>
      </linearGradient>
      <linearGradient id="portraitTone" x1="0" y1="0" x2="1" y2="1">
        <stop offset="0" stop-color="#ececec"/>
        <stop offset="0.55" stop-color="#5a5a5a"/>
        <stop offset="1" stop-color="#1e1e1e"/>
      </linearGradient>
      <radialGradient id="garmentTone" cx="0.5" cy="0.5" r="0.6">
        <stop offset="0" stop-color="#3a3a3a"/>
        <stop offset="1" stop-color="#e8e8e8"/>
      </radialGradient>
    </defs>

    <rect class="band-top" x="0" y="0" width="963" height="28" fill="#1b1b1b"/>
    <rect class="panel-dark" x="0" y="479" width="963" height="721" fill="url(#darkPanel)"/>
    <rect class="band-green" x="0" y="469" width="963" height="10" fill="#1fa33a"/>
    <line class="brand-rule" x1="22" y1="198" x2="500" y2="198" stroke="#e4e4e4" stroke-width="2"/>

    <polygon class="feature-frame" points="452,391 643,59 963,59 963,727 643,727" fill="#1b1b1b"/>
    <polygon class="feature-ring" points="478,391 656,72 963,72 963,711 656,711" fill="#1fa33a"/>
    <polygon class="feature-gap" points="504,391 676,84 963,84 963,692 676,692" fill="#ffffff"/>
    <polygon class="feature-photo" role="img" aria-label="Photo of a man wearing a black leather work jacket"
             points="513,391 682,91 963,91 963,683 682,683" fill="url(#portraitTone)"/>

    <polygon class="hours-tab" points="530,777 963,777 963,825 550,825" fill="#d9d9d9"/>

    <polygon class="product-hex" points="39,896 91,809 193,809 245,896 193,983 91,983" fill="#ffffff" stroke="#1fa33a" stroke-width="4"/>
    <polygon class="product-photo" role="img" aria-label="Black insulated work vest"
             points="52,896 98,820 186,820 232,896 186,972 98,972" fill="url(#garmentTone)"/>
    <polygon class="product-hex" points="287,896 339,809 441,809 493,896 441,983 339,983" fill="#ffffff" stroke="#1fa33a" stroke-width="4"/>
    <polygon class="product-photo" role="img" aria-label="Black hooded work jacket"
             points="300,896 346,820 434,820 480,896 434,972 346,972" fill="url(#garmentTone)"/>

    <polyline class="footer-rule" points="0,1157 500,1157 565,1092 963,1092" fill="none" stroke="#ffffff" stroke-width="4"/>
    <polygon class="footer-band" points="0,1168 510,1168 575,1103 963,1103 963,1200 0,1200" fill="#1fa33a"/>
  </svg>

  <header class="brand">
    <div class="brand__mark"></div>
    <div class="brand__name">Northgate<br>Bolts &amp; Tools</div>
  </header>

  <section class="headline">
    <h1 class="headline__main">Save Time</h1>
    <p class="headline__sub">Buy Online</p>
  </section>

  <section class="validity">
    <p class="validity__lead">Prices Valid</p>
    <p class="validity__month">Until December</p>
    <p class="validity__date"><span class="validity__day">31st</span> <span class="validity__year">2015</span></p>
  </section>

  <h2 class="hours__title">Hours of Operation</h2>
  <section class="hours__list">
    <p class="hours__day">Mon-Fri</p>
    <p class="hours__time">6:30AM - 5:00PM</p>
    <p class="hours__day">Saturday</p>
    <p class="hours__time">7:30AM - 12:00PM</p>
  </section>

  <section class="partners">
    <div class="partner">Corvel</div>
    <div class="partner"><span class="partner__square"></span>Dustbox</div>
  </section>

  <address class="contact">
    <div class="contact__row">306-555-0142
      <svg class="contact__icon" viewBox="0 0 16 16"><path d="M4 2 L6 2 L7 5 L5.5 6.5 Q7 9.5 9.5 10.5 L11 9 L14 10 L14 12 Q13 14 11 14 Q3 12 2 4 Q2 2 4 2 Z"/></svg>
      &nbsp;www.qr-w.example
      <svg class="contact__icon" viewBox="0 0 16 16"><circle cx="8" cy="8" r="6"/><path d="M2 8 H14 M8 2 Q4 8 8 14 M8 2 Q12 8 8 14"/></svg>
    </div>
    <div class="contact__row">218 12b Street East Riverton,
      <svg class="contact__icon" viewBox="0 0 16 16"><path d="M8 15 Q3 9 3 6 A5 5 0 0 1 13 6 Q13 9 8 15 Z"/><circle cx="8" cy="6" r="1.8"/></svg>
    </div>
    <div class="contact__row contact__row--last">SK, Canada S0K 1A0</div>
  </address>
</main>
</body>
</html>
```